Etiketten für prämierte BBQ Sauce
tr Grafikstube arbeitet sehr professionell und ist sehr hilfsbereit
Zielgruppe
Wir sind ein junges erfolgreiches BBQ Team und suchen für unsere prämierte Sauce ein Etikett.
Aufgabenstellung
Es ist eine Flasche mit 263 ml, der Umfang ist 18 cm, Höhe für das Etikett 6cm (wobei anhand der Aussparung 5.8 besser wäre). Es muss nicht die ganze Flasche umschliessen
Deckel max. 2.6 im Durchmesser
Folgende Infos müssen ersichtlich sein
Honey Mustard Sauce
263ml
Zutatenliste: Senf, Honig, Ketchup, Gewürze, Zucker, Natürliche Aromen, Essig
Mindesthaltbarkeit
Nach dem Öffnen im Kühlschrank aufbewahren
Like us on Plaudernet
Es wäre schön, wenn sich das Logo im Etikett einbetten würde, muss aber nicht. Jedoch sollte es dann zumindest irgendwo bei den Zutaten oder so ersichtlich sein. Mir persönlich schwebte mal etwas im Stil von Kreide vor so quasi das Logo monochrom mit Kreide. Jedoch ist das auch kein muss es soll aber aufzeigen, dass das Logo auch schwarz/weiss sein darf. Dies ist nur mal eine Idee welche ich hatte aber ich überlasse der Creativen Crowd die Freiheit das Etikett zu gestalten :-)
Bei Fragen einfach melden

```html
<!DOCTYPE html>
<html lang="de">
<head>
<meta charset="utf-8">
<title>Honey Mustard Sauce – Etiketten</title>
<link rel="stylesheet" href="https://fonts.googleapis.com/css2?family=Abril+Fatface&family=Big+Shoulders+Display:wght@900&family=Encode+Sans+Condensed:wght@400;700&family=Rye&family=Yellowtail&display=swap">
<style>
  :root {
    --bg-light: #f6f6f6;
    --bg-dark: #e2e2e2;
    --chalk-1: #2e2e2e;
    --chalk-2: #1b1b1b;
    --chalk-white: #ffffff;
    --ink: #222222;
  }
  html, body {
    margin: 0;
    width: 1200px;
    height: 827px;
    overflow: hidden;
    background: radial-gradient(ellipse at 50% 35%, var(--bg-light), var(--bg-dark));
  }
  .sheet { display: block; width: 1200px; height: 827px; }
  .frame-outer { fill: none; stroke: var(--chalk-white); stroke-width: 2.5; }
  .frame-inner { fill: none; stroke: var(--chalk-white); stroke-width: 3.5; }
  .rule { stroke: var(--chalk-white); stroke-width: 2; }
  .script { font-family: "Yellowtail", cursive; fill: var(--chalk-white); }
  .headline-honey { font-family: "Big Shoulders Display", sans-serif; font-weight: 900; fill: var(--chalk-white); }
  .headline-mustard { font-family: "Abril Fatface", serif; fill: var(--chalk-white); }
  .headline-sauce { font-family: "Rye", serif; fill: var(--ink); }
  .western { font-family: "Rye", serif; fill: var(--chalk-white); }
  .body-copy { font-family: "Encode Sans Condensed", sans-serif; fill: var(--chalk-white); }
  .volume { font-family: "Encode Sans Condensed", sans-serif; font-weight: 700; fill: var(--chalk-white); }
  .brand-name { font-family: "Encode Sans Condensed", sans-serif; font-weight: 700; fill: var(--chalk-white); }
</style>
</head>
<body>
<svg class="sheet" viewBox="0 0 1200 827" xmlns="http://www.w3.org/2000/svg">
  <defs>
    <linearGradient id="chalk" x1="0" y1="0" x2="1" y2="1">
      <stop offset="0" stop-color="var(--chalk-1)"/>
      <stop offset="1" stop-color="var(--chalk-2)"/>
    </linearGradient>
  </defs>

  <g class="label-front">
    <rect x="174" y="179" width="387" height="501" rx="22" fill="url(#chalk)"/>
    <rect class="frame-outer" x="188" y="192" width="359" height="475" rx="24"/>
    <rect class="frame-inner" x="203" y="206" width="329" height="447" rx="20"/>

    <g class="brand-tab">
      <circle cx="368" cy="199" r="52" fill="url(#chalk)"/>
      <circle cx="368" cy="199" r="45" fill="none" stroke="var(--chalk-white)" stroke-width="2.5"/>
      <text class="brand-name" x="368" y="204" font-size="14" text-anchor="middle" textLength="72" lengthAdjust="spacingAndGlyphs">FUNKENWERK</text>
    </g>

    <line class="rule" x1="222" y1="296" x2="286" y2="296"/>
    <line class="rule" x1="452" y1="296" x2="516" y2="296"/>
    <text class="script" x="369" y="305" font-size="30" text-anchor="middle">the original</text>

    <text class="headline-honey" x="369" y="414" font-size="118" text-anchor="middle" textLength="294" lengthAdjust="spacingAndGlyphs">HONEY</text>

    <line class="rule" x1="222" y1="425" x2="512" y2="425"/>
    <line class="rule" x1="222" y1="431" x2="512" y2="431"/>
    <line class="rule" x1="222" y1="438" x2="512" y2="438"/>

    <text class="headline-mustard" x="369" y="494" font-size="50" text-anchor="middle" textLength="294" lengthAdjust="spacingAndGlyphs">MUSTARD</text>

    <rect x="203" y="508" width="329" height="75" fill="var(--chalk-white)"/>
    <path d="M222 548 Q250 542 290 547 Q250 553 222 548 Z" fill="var(--ink)"/>
    <path d="M514 548 Q486 542 446 547 Q486 553 514 548 Z" fill="var(--ink)"/>
    <text class="headline-sauce" x="369" y="564" font-size="38" text-anchor="middle">SAUCE</text>
  </g>

  <g class="label-back">
    <rect x="639" y="176" width="386" height="503" rx="22" fill="url(#chalk)"/>
    <rect class="frame-outer" x="653" y="190" width="358" height="475" rx="24"/>
    <rect class="frame-inner" x="668" y="204" width="328" height="448" rx="20"/>

    <g class="stamp">
      <circle cx="831" cy="277" r="62" fill="none" stroke="var(--chalk-white)" stroke-width="3"/>
      <circle cx="831" cy="277" r="55" fill="none" stroke="var(--chalk-white)" stroke-width="1.5"/>
      <text class="script" x="831" y="249" font-size="20" text-anchor="middle">with</text>
      <rect x="772" y="257" width="118" height="40" rx="5" fill="url(#chalk)" stroke="var(--chalk-white)" stroke-width="2.5"/>
      <text class="headline-honey" x="831" y="289" font-size="32" text-anchor="middle" textLength="104" lengthAdjust="spacingAndGlyphs">HONEY &amp;</text>
      <rect x="785" y="301" width="92" height="24" rx="4" fill="url(#chalk)" stroke="var(--chalk-white)" stroke-width="2"/>
      <text class="headline-mustard" x="831" y="319" font-size="16" text-anchor="middle" textLength="80" lengthAdjust="spacingAndGlyphs">MUSTARD</text>
    </g>

    <text class="script" x="831" y="375" font-size="22" text-anchor="middle">Zutaten</text>
    <text class="body-copy" x="831" y="398" font-size="15.5" text-anchor="middle">Senf, Honig, Ketchup, Gewürze, Zucker,</text>
    <text class="body-copy" x="831" y="420" font-size="15.5" text-anchor="middle">Natürliche Aromen, Essig</text>

    <line class="rule" x1="687" y1="430" x2="973" y2="430"/>
    <line class="rule" x1="687" y1="437" x2="973" y2="437"/>
    <line class="rule" x1="687" y1="446" x2="973" y2="446"/>

    <text class="body-copy" x="831" y="471" font-size="15.5" text-anchor="middle">Nach dem Öffnen im Kühlschrank aufbewahren</text>

    <g class="brand-social">
      <circle cx="733" cy="531" r="34" fill="none" stroke="var(--chalk-white)" stroke-width="2"/>
      <text class="brand-name" x="733" y="535" font-size="12" text-anchor="middle" textLength="56" lengthAdjust="spacingAndGlyphs">FUNKENWERK</text>
      <text class="western" x="776" y="535" font-size="14.5" textLength="198" lengthAdjust="spacingAndGlyphs">LIKE US ON PLAUDERNET!</text>
    </g>

    <text class="body-copy" x="977" y="586" font-size="15.5" text-anchor="end">Mindestens haltbar bis:</text>
    <text class="volume" x="687" y="632" font-size="34">263<tspan font-size="26" dx="4">ml</tspan></text>
    <rect x="831" y="597" width="155" height="83" fill="var(--chalk-white)"/>
  </g>
</svg>
</body>
</html>
```